Brochure design for 3D ultrasound company

I am looking for a clean and modern and edgy brochure for my ultrasound company. We are a fairly new company specialize in 3D/4D ultrasounds.Our brochures will be placed in OB-GYN offices in high end areas around Los Angeles, so we need something that will stand out and capture a modern woman's attention. Our logo is currently in the process of being designed, so I don't have a picture to provide quite yet, however it will be our company name"Kite + Fern" written in a special font that looks like neon lights. I will attach a few images of what our logo will be like, and some initial content that can help provide the layout we would like for the brochure. please feel free to also take a look at our website. www.kitefernscans.example.

Target Market(s)

Upscale trendy women.

Colors
eea4c8
33a6d7
fee18a

Requirements
Should not have
• too many colors.

```html
<!DOCTYPE html>
<html lang="en">
<head>
<meta charset="utf-8">
<title>Kite + Fern brochure</title>
<link rel="stylesheet" href="https://fonts.googleapis.com/css2?family=Montserrat:wght@400;500;600;700&family=Open+Sans:wght@400;600&display=swap">
<style>
:root{
  --pink:#eea4c8;
  --pink-deep:#e282b1;
  --pink-soft:#fbe3ef;
  --ink:#4a4a4a;
  --muted:#7a7a7a;
  --paper:#ffffff;
  --backdrop:#e9e9ec;
  --photo-warm:#d9b8a8;
  --photo-dark:#3b3338;
}
*{box-sizing:border-box;margin:0;padding:0}
html,body{width:880px;height:1200px;overflow:hidden;background:var(--backdrop)}
body{font-family:"Open Sans",sans-serif;color:var(--ink);position:relative}
.sheet{position:absolute;left:20px;width:840px;height:570px;background:var(--paper);display:flex;box-shadow:0 2px 8px rgba(0,0,0,.12)}
.sheet--outside{top:20px}
.sheet--inside{top:610px}
.panel{width:280px;height:100%;position:relative;overflow:hidden;border-right:1px solid #eee}
.panel:last-child{border-right:none}
.photo{position:absolute;left:0;width:100%}
.wave{position:absolute;left:0;width:100%}
.body{position:absolute;left:22px;right:22px}
h2{font-family:"Montserrat",sans-serif;font-size:13px;font-weight:700;color:var(--ink);letter-spacing:.5px;margin-bottom:8px}
h3{font-family:"Montserrat",sans-serif;font-size:10px;font-weight:700;color:var(--pink-deep);letter-spacing:.5px;margin:8px 0 4px}
p{font-size:8.5px;line-height:1.5;color:var(--muted);margin-bottom:6px}
ul{list-style:none}
li{font-size:8.5px;line-height:1.55;color:var(--muted)}
li::before{content:"•";color:var(--pink-deep);margin-right:5px}
.pill{display:inline-block;background:var(--pink);color:#fff;font-family:"Montserrat",sans-serif;font-size:8.5px;font-weight:600;padding:4px 12px;border-radius:12px}
.brand{font-family:"Montserrat",sans-serif;font-weight:600;color:var(--ink);font-size:26px;letter-spacing:.5px}
.tagline{font-size:8.5px;color:var(--muted);margin-top:2px}
.contact-line{font-size:8.5px;color:var(--muted);margin-top:4px}
.dot{display:inline-block;width:14px;height:14px;border-radius:50%;background:var(--pink);margin-right:5px}
.band{position:absolute;left:0;width:100%;background:var(--pink);color:#fff;font-family:"Montserrat",sans-serif;font-weight:600;text-align:center}
.price-row{display:flex;justify-content:flex-end;margin-top:3px}
</style>
</head>
<body>

<section class="sheet sheet--outside">
  <div class="panel">
    <div class="photo" role="img" aria-label="Ultrasound scan being shown on a belly" style="top:0;height:150px;background:linear-gradient(135deg,var(--photo-warm),var(--photo-dark))"></div>
    <svg class="wave" style="top:120px" width="280" height="40" viewBox="0 0 280 40"><path d="M0 30 Q140 -10 280 22 L280 40 L0 40Z" fill="var(--pink)"/><path d="M0 36 Q140 2 280 30 L280 40 L0 40Z" fill="#fff"/></svg>
    <div class="body" style="top:172px">
      <h2>WHAT'S WHAT...</h2>
      <p><b style="color:var(--pink-deep)">2D</b> is the traditional black and white ultrasound image. This is what you usually see at your doctor's office.</p>
      <p><b style="color:var(--pink-deep)">3D</b> is an image of the baby taken in three planes, so you can see the features that make your little one unique.</p>
      <p><b style="color:var(--pink-deep)">4D</b> is 3D with motion. You can watch your baby yawn, stretch and smile in real time.</p>
      <p><b style="color:var(--pink-deep)">HD Live</b> is 3D with realistic lighting and skin tones, giving the most lifelike view of your baby that we can offer.</p>
      <div style="margin-top:10px"><span class="pill">Call today! (555) 014-2290</span></div>
      <div class="contact-line">www.kitefernscans.example</div>
    </div>
  </div>

  <div class="panel">
    <div class="body" style="top:36px">
      <div class="brand">Kite + Fern</div>
      <div class="tagline">A mobile 3D/4D ultrasound service</div>
      <p style="margin-top:14px">Kite + Fern is a mobile 3D/4D ultrasound company servicing Los Angeles and surrounding areas.</p>
      <p>We take great pride in being one of LA's first mobile ultrasound companies and in being an all female business.</p>
      <h2 style="margin-top:14px">OUR MISSION</h2>
      <p>Our mission is to provide an unforgettable experience for expectant mothers in the comfort of their homes.</p>
      <h2 style="margin-top:16px">CONTACT US</h2>
      <span class="pill">Call today! (555) 014-2290</span>
      <div class="contact-line">www.kitefernscans.example</div>
      <div class="contact-line">hello@kitefernscans.example</div>
      <div style="margin-top:10px"><span class="dot"></span><span class="dot"></span></div>
    </div>
  </div>

  <div class="panel">
    <div class="body" style="top:26px">
      <div class="brand" style="color:var(--pink-deep)">Kite + Fern</div>
      <div class="tagline">A mobile 3D/4D ultrasound service</div>
    </div>
    <div class="photo" role="img" aria-label="Strip of ultrasound prints" style="top:92px;left:70px;width:190px;height:44px;background:linear-gradient(90deg,#2e2a2c,#6b6266)"></div>
    <div class="photo" role="img" aria-label="Pregnant woman sitting on a bed" style="top:150px;height:300px;background:linear-gradient(160deg,#f3ecea,var(--photo-warm))"></div>
    <svg class="wave" style="top:420px" width="280" height="40" viewBox="0 0 280 40"><path d="M0 10 Q140 40 280 8 L280 40 L0 40Z" fill="var(--pink)"/></svg>
    <div class="band" style="top:458px;height:40px;font-size:12px;padding-top:5px">Ultrasound in the comfort<br>of your home</div>
    <div class="body" style="top:514px;text-align:right">
      <span class="pill">Call today! (555) 014-2290</span>
    </div>
  </div>
</section>

<section class="sheet sheet--inside">
  <div class="panel">
    <div class="photo" role="img" aria-label="Expecting couple embracing" style="top:0;height:150px;background:linear-gradient(135deg,var(--photo-dark),var(--photo-warm))"></div>
    <svg class="wave" style="top:120px" width="280" height="40" viewBox="0 0 280 40"><path d="M0 22 Q140 -8 280 30 L280 40 L0 40Z" fill="var(--pink)"/><path d="M0 30 Q140 4 280 36 L280 40 L0 40Z" fill="#fff"/></svg>
    <div class="body" style="top:166px">
      <h2>SERVICES + PRICING</h2>
      <p>We are available for private in-home screenings, gender reveals, baby showers, or any other special occasion.</p>
      <h3>PEEK A BOO</h3>
      <ul><li>10 minute 3D/4D session</li><li>5 black and white images</li><li>Listen to baby's heartbeat</li></ul>
      <div class="price-row"><span class="pill">$99</span></div>
      <h3>HELLO, BABY</h3>
      <ul><li>15 minute 3D/4D HD live scan</li><li>Gender determination</li><li>5 color images</li><li>Listen to baby's heartbeat</li></ul>
      <div class="price-row"><span class="pill">$149</span></div>
      <h3>A LITTLE IMPORTANT BABY</h3>
      <ul><li>30 min 3D/4D/HD live session</li><li>10 color images</li><li>Email or USB with all images</li><li>Record and hear heartbeat</li><li>Confirm gender</li></ul>
    </div>
  </div>

  <div class="panel">
    <div class="photo" role="img" aria-label="3D ultrasound image of a baby" style="top:0;height:130px;background:linear-gradient(135deg,#c99a6e,#5a3c2c)"></div>
    <div class="body" style="top:146px">
      <h3>BABY BUNDLE</h3>
      <ul><li>20 minute 3D/4D session</li><li>8 color images</li><li>Heartbeat recording</li><li>Confirm gender</li></ul>
      <div class="price-row"><span class="pill">$199</span></div>
      <h3>GENDER REVEAL</h3>
      <ul><li>Gender check from 15 weeks</li><li>2 black and white images</li><li>Sealed envelope for reveal</li></ul>
      <div class="price-row"><span class="pill">$79</span></div>
    </div>
    <div class="photo" role="img" aria-label="Mother holding ultrasound print" style="top:390px;height:180px;background:linear-gradient(160deg,var(--pink-soft),var(--photo-warm))"></div>
  </div>

  <div class="panel">
    <div class="body" style="top:24px">
      <div class="brand" style="color:var(--pink-deep)">Kite + Fern</div>
      <h2 style="margin-top:18px;text-align:center">OUR MOST POPULAR<br>PACKAGE</h2>
      <h3>BIG BABY BUNDLE</h3>
      <ul><li>30 minute 3D/4D session</li><li>5 black and white prints</li><li>5 color prints</li><li>Email or USB with all images</li><li>Record and hear heartbeat</li><li>Confirm gender</li></ul>
      <div class="price-row"><span class="pill">$249</span></div>
    </div>
    <div class="photo" role="img" aria-label="Pregnant woman cradling her belly" style="top:300px;left:22px;width:236px;height:120px;background:linear-gradient(135deg,#f4eeee,var(--photo-warm))"></div>
    <div class="body" style="top:436px;text-align:center">
      <h2>READY FOR YOUR BABY'S<br>FIRST PHOTOSHOOT?</h2>
      <p>Give us a call to schedule an appointment with us today!</p>
      <span class="pill">(555) 014-2290</span>
      <div class="contact-line">www.kitefernscans.example</div>
    </div>
  </div>
</section>

</body>
</html>
```